Brindlewave Systems Website Project

We require a design to revamp and existing website for a company that provides online solutions for small the medium sized businesses including web development, online marketing, social media, online business plans, social media and e-commerce. We are looking to use colours that integrate well with the current logo. Our target market are small to medium sized businesses and individuals looking for a trusted adviser to cover all their online services.
Existing website - www.brindlewavesystems.com.au
Updates
Participation payments added.
Storyboard layout mentioned in brief was not attached in error. It will be uploaded shortly.
Storyboard file added.
Target Market(s)
Revamp of existing website - Looking for a professional design in line with the target market of small to medium businesses
Industry/Entity Type
Business
Requirements
Must have
- Refer the attached storyboard layout for the site design and requirements. Basic header, footer and sidebar are to be the same on every page with the content changing to match the requirements on each page. 8 pages in total
Should not have
- No click here text

```html
<!DOCTYPE html>
<html lang="en">
<head>
<meta charset="utf-8">
<title>Brindlewave Systems – Online Solutions</title>
<link href="https://fonts.googleapis.com/css2?family=Source+Sans+3:wght@400;600;700&family=Arimo:wght@400;700&display=swap" rel="stylesheet">
<style>
:root{
  --green:#4cb944;
  --green-dark:#2e9a2a;
  --green-deep:#139a22;
  --lime:#8cc63f;
  --yellow:#f5f20a;
  --ink:#1d1d1d;
  --text:#444;
  --panel:#d4d4d6;
  --footer:#333;
  --white:#fff;
}
*{margin:0;padding:0;box-sizing:border-box}
html,body{width:856px;height:1200px;overflow:hidden;background:#fafafa}
body{position:relative;font-family:"Source Sans 3",sans-serif;color:var(--text)}
.abs{position:absolute}
.topbar{left:0;top:0;width:856px;height:24px;background:var(--green);color:var(--white);font-size:9px;line-height:24px;text-align:right;padding-right:110px}
.topbar b{font-weight:700}
.topbar .tel{color:var(--ink);margin-left:12px}
.brand{left:110px;top:48px;display:flex;align-items:center;gap:8px}
.brand-mark{width:34px;height:34px;border-radius:50%;background:var(--green)}
.brand-name{font-size:22px;font-weight:600;color:var(--ink);line-height:1.05}
.tagline{left:293px;top:82px;font-size:25px;color:var(--ink);letter-spacing:-.5px}
.tagline span{color:var(--green)}
.nav{left:100px;top:170px;width:656px;height:23px;border-top:2px solid var(--green);border-bottom:2px solid var(--green);display:flex;align-items:center;font-size:8.5px;color:var(--green-dark);text-transform:uppercase}
.nav a{color:inherit;text-decoration:none;padding:0 17px;line-height:19px}
.nav a.active{background:var(--green);color:var(--white);padding:0 24px}
.hero{left:100px;top:205px;width:656px;height:180px;background:linear-gradient(90deg,#7ab82e 0%,#9ccc3a 35%,#8bc53f 100%);border:1px solid #6aa52a}
.hero-photo{left:0;top:0;width:260px;height:178px;background:radial-gradient(circle at 45% 50%,#d9d2c0 0,#b9a68a 30%,#5e9a25 70%,#7ab82e 100%)}
.hero-title{left:250px;top:4px;width:400px;text-align:center;font-family:Arimo,sans-serif;font-weight:700;font-size:33px;line-height:42px;color:var(--white)}
.hero-title span{color:var(--yellow)}
.hero-sub{left:290px;top:94px;width:320px;text-align:center;font-family:Arimo,sans-serif;font-size:18px;line-height:25px;color:var(--white)}
.dots{left:380px;top:387px;width:96px;height:16px;background:var(--green);display:flex;justify-content:center;align-items:center;gap:6px}
.dots i{width:7px;height:7px;border-radius:50%;background:var(--white)}
.dots i:first-child{background:#111;box-shadow:0 0 0 1.5px var(--white)}
.svc{width:206px}
.svc h3{font-size:14px;font-weight:600;color:var(--green);text-transform:uppercase;padding-left:74px;height:17px}
.svc .box{position:relative;height:83px;background:linear-gradient(180deg,#5cc24c,#3aaa36);color:var(--white);font-size:9px;line-height:13px;padding:11px 10px 0 73px}
.svc .art{position:absolute;left:2px;top:-14px;width:66px;height:92px;background:radial-gradient(ellipse at 50% 55%,#ff7a2a 0,#f0a52a 35%,rgba(60,170,54,0) 70%)}
.svc .more{position:absolute;right:0;bottom:-4px;background:#111;color:var(--white);font-size:7.5px;font-weight:700;font-style:italic;padding:1px 5px}
.why-title{left:105px;top:660px;font-size:26px;color:var(--green)}
.why-text{left:105px;top:699px;width:428px;font-size:8.4px;line-height:18.8px;color:#333}
.rule{left:100px;top:868px;width:432px;height:1px;background:#cde6c6}
.quote{left:550px;top:656px;width:206px;height:217px;background:var(--panel)}
.quote h2{position:absolute;left:14px;top:6px;font-size:25px;font-weight:400;color:#333;letter-spacing:-.3px}
.quote .row{position:absolute;left:0;width:206px;font-size:10px;color:#333}
.quote .row label{position:absolute;right:148px;top:2px}
.quote .row span{position:absolute;left:58px;width:134px;height:17px;background:var(--white);border:1px solid #aaa}
.quote .box-mail{position:absolute;left:8px;top:158px;width:46px;height:58px;background:linear-gradient(180deg,#666,#2a2a2a);border-radius:16px 16px 2px 2px}
.quote .send{position:absolute;right:14px;top:186px;background:#111;color:var(--white);font-size:8px;font-weight:700;font-style:italic;padding:2px 7px}
.browse{left:105px;top:884px;font-size:26px;color:var(--ink);letter-spacing:-.6px}
.arrow{top:953px;width:12px;height:31px;background:var(--green);color:var(--white);font-size:14px;line-height:31px;text-align:center}
.thumb{top:931px;width:117px;height:75px;border:1px solid #8fd487;background:var(--white);display:flex;flex-direction:column;align-items:center;justify-content:center;text-align:center;font-size:13px;color:#333;overflow:hidden}
.thumb small{font-size:6px;color:#c7751f}
.thumb.soon{background:var(--green-deep);border-color:var(--green-deep);color:#7bd36c;font-weight:700;font-size:11px;line-height:13px}
.footer{left:0;top:1036px;width:856px;height:137px;background:var(--footer);color:var(--white)}
.footer h4{position:absolute;top:10px;font-size:13.5px;font-weight:700}
.footer ul{position:absolute;left:120px;top:38px;list-style:none;font-size:7.5px;line-height:12px}
.social{position:absolute;left:377px;top:42px;display:flex;gap:9px}
.social i{width:23px;height:23px;border-radius:3px;background:#3f6fb0}
.social i:nth-child(2){background:#2fb3e0}
.social i:nth-child(3){background:#1f7fc0}
.social i:nth-child(4){background:#2a9ad8}
.foot-brand{position:absolute;left:592px;top:55px;display:flex;align-items:center;gap:7px;font-size:17px;font-weight:600;color:#666}
.foot-brand b{width:24px;height:24px;border-radius:50%;background:#555}
.copy{left:108px;top:1179px;font-size:8.5px;color:#333}
</style>
</head>
<body>
<div class="abs topbar"><b>EMAIL :</b> contact@brindlewavesystems.com.au <span class="tel"><b>TEL:</b> 0491 570 156</span></div>

<div class="abs brand"><span class="brand-mark"></span><span class="brand-name">Brindlewave<br>Systems</span></div>
<div class="abs tagline">Leading the Way in <span>ONLINE SOLUTIONS</span></div>

<nav class="abs nav">
  <a class="active">Home</a><a>About Us</a><a>Services</a><a>Portfolio</a><a>Individual Service</a><a>Individual Portfolio</a><a>Contact</a><a>Blog</a>
</nav>

<section class="abs hero">
  <div class="abs hero-photo" role="img" aria-label="Hand holding a compass against a green background"></div>
  <h1 class="abs hero-title">Make <span>navigating</span> your business online easy</h1>
  <p class="abs hero-sub">We provide ongoing service to ensure we are delivering the best solution for your business</p>
</section>
<div class="abs dots"><i></i><i></i><i></i><i></i><i></i><i></i></div>

<div class="abs svc" style="left:100px;top:414px"><h3>Blogs</h3><div class="box"><div class="art" role="img" aria-label="Figure with speech bubbles"></div>Need a dynamic blog to compliment your business or want a blog for personal expression?<span class="more">Find Out More</span></div></div>
<div class="abs svc" style="left:326px;top:414px"><h3>Social Media</h3><div class="box"><div class="art" role="img" aria-label="Two figures shaking hands"></div>Fast track business success through the use of social media solutions and strategies.<span class="more">Find Out More</span></div></div>
<div class="abs svc" style="left:550px;top:414px"><h3>Web Development</h3><div class="box"><div class="art" role="img" aria-label="Figure holding tools"></div>Website solutions designed and developed to maximise your online footprint.<span class="more">Find Out More</span></div></div>
<div class="abs svc" style="left:100px;top:531px"><h3>E-Commerce</h3><div class="box"><div class="art" role="img" aria-label="Figure pushing a shopping cart"></div>E-commerce solutions tailored to your business goals and objectives to help drive sales.<span class="more">Find Out More</span></div></div>
<div class="abs svc" style="left:326px;top:531px"><h3>Online Business</h3><div class="box"><div class="art" role="img" aria-label="Figure working at a desk computer"></div>Online specific business plans designed to help you take your idea to the next level.<span class="more">Find Out More</span></div></div>
<div class="abs svc" style="left:550px;top:531px"><h3>Online Marketing</h3><div class="box"><div class="art" role="img" aria-label="Figure carrying a light bulb"></div>Online marketing solutions developed to enhance your website and grow your business.<span class="more">Find Out More</span></div></div>

<h2 class="abs why-title">Why Choose us?</h2>
<p class="abs why-text">Website solutions tailored to your business cost effective pricing to suit your budget strategies to support your online presence Regular maintenance packages available Prefessional design and development Online business plans to promote growth SEO techniques incorporated into all solutions Online marking options available blogs and e-commerce solutions available.  Website solutions tailored to your business cost effective pricing to suit your budget strategies to support your online presence Regular maintenance packages available Professional design and development Online business plans to promote growth SEO techniques incorporated into all solutions Online marking options available blogs and e-commerce solutions available.</p>
<div class="abs rule"></div>

<aside class="abs quote">
  <h2>Request A Quota</h2>
  <div class="row" style="top:44px"><label>Name :</label><span></span></div>
  <div class="row" style="top:69px"><label>Email :</label><span></span></div>
  <div class="row" style="top:93px"><label>Phone :</label><span></span></div>
  <div class="row" style="top:117px"><label>Message :</label><span style="height:66px"></span></div>
  <div class="box-mail" role="img" aria-label="Mailbox"></div>
  <span class="send">Please Contact Me</span>
</aside>

<h2 class="abs browse">Browse Our Recent Work</h2>
<div class="abs arrow" style="left:100px">‹</div>
<div class="abs arrow" style="left:744px">›</div>
<div class="abs thumb" style="left:111px;background:#cfe8c8" role="img" aria-label="Restaurant website preview">Qamra</div>
<div class="abs thumb" style="left:241px">Tallow Marketing<small>Coming Soon</small></div>
<div class="abs thumb" style="left:370px;background:#e3ecf3" role="img" aria-label="Event design website preview">Elm Arthouse</div>
<div class="abs thumb" style="left:499px;background:linear-gradient(180deg,#fff 0 58%,#f1dc5a 58% 72%,#fff 72%)" role="img" aria-label="Arthouse journal page preview">Elm Arthouse</div>
<div class="abs thumb soon" style="left:628px">MORE COMING<br>SOON</div>

<footer class="abs footer">
  <h4 style="left:120px">CHECK OUT OUR SERVICES</h4>
  <ul>
    <li>WEB DESIGN AND DEVELOPMENT</li><li>SEARCH ENGINE OPTIMISATION</li><li>ONLINE BUSINESS CONSULTANTS</li><li>ONLINE MARKETING</li><li>SOCIAL MEDIA</li><li>E-COMMERCE</li><li>BLOGS</li>
  </ul>
  <h4 style="left:377px">FOLLOW US</h4>
  <div class="social"><i></i><i></i><i></i><i></i></div>
  <div class="foot-brand"><b></b>Brindlewave Systems</div>
</footer>
<p class="abs copy">© ALL RIGHTS RESERVED BRINDLEWAVE SYSTEMS 2011</p>
</body>
</html>
```